Tirovel

We need a business card for our company is a holding for different business all are different we try to have some air of relax and fun in our projects we add pictures of the office to give you an idea od the mood of the business

Business

```html
<!DOCTYPE html>
<html lang="en">
<head>
<meta charset="utf-8">
<title>Tirovel — Business Card</title>
<link rel="stylesheet" href="https://fonts.googleapis.com/css2?family=Ubuntu:wght@400;500;700&display=swap">
<style>
  :root {
    --backdrop: #e6e6e8;
    --paper: #ffffff;
    --sun: #f2e632;
    --cocoa: #5b3a12;
    --cocoa-text: #5b3a12;
  }
  * { box-sizing: border-box; margin: 0; padding: 0; }
  html, body {
    width: 1200px;
    height: 810px;
    overflow: hidden;
    background: var(--backdrop);
    font-family: "Ubuntu", sans-serif;
  }
  .stage {
    width: 1200px;
    height: 810px;
    display: flex;
    align-items: center;
    justify-content: center;
  }
  .card {
    position: relative;
    width: 700px;
    height: 400px;
    background: var(--paper);
    display: grid;
    grid-template-columns: 1fr 1fr;
    box-shadow: 0 10px 30px rgba(0,0,0,0.10);
  }
  .brand-side {
    display: flex;
    align-items: center;
    justify-content: center;
    gap: 16px;
    background: var(--paper);
  }
  .brand-mark {
    width: 44px;
    height: 44px;
    background: var(--sun);
  }
  .brand-name {
    font-weight: 700;
    font-size: 56px;
    letter-spacing: -1px;
    color: var(--cocoa-text);
    line-height: 1;
  }
  .info-side {
    background: var(--sun);
    padding-top: 62px;
  }
  .name-band {
    background: var(--cocoa);
    color: var(--sun);
    height: 40px;
    display: flex;
    align-items: center;
    padding-left: 40px;
    font-size: 21px;
    font-weight: 500;
  }
  .contact-list {
    list-style: none;
    padding: 30px 0 0 40px;
  }
  .contact-list li {
    display: flex;
    align-items: center;
    gap: 14px;
    font-size: 17px;
    color: var(--cocoa-text);
    height: 32px;
  }
  .contact-list .address-lines {
    display: flex;
    flex-direction: column;
    line-height: 1.3;
  }
  .contact-list li.address { height: 52px; }
  .contact-icon { width: 18px; height: 18px; flex: none; }
</style>
</head>
<body>
<main class="stage">
  <article class="card">
    <section class="brand-side">
      <span class="brand-mark"></span>
      <span class="brand-name">Tirovel</span>
    </section>
    <section class="info-side">
      <div class="name-band">Mara Quell</div>
      <ul class="contact-list">
        <li class="address">
          <svg class="contact-icon" viewBox="0 0 18 18" aria-hidden="true">
            <path d="M9 1.5c-3 0-5.2 2.2-5.2 5.1 0 3.6 5.2 9.9 5.2 9.9s5.2-6.3 5.2-9.9C14.2 3.7 12 1.5 9 1.5z" fill="var(--cocoa)"/>
            <circle cx="9" cy="6.6" r="2" fill="var(--sun)"/>
          </svg>
          <span class="address-lines">
            <span>14 Orchard Lane</span>
            <span>Suite 2, Riverton</span>
          </span>
        </li>
        <li>
          <svg class="contact-icon" viewBox="0 0 18 18" aria-hidden="true">
            <circle cx="9" cy="9" r="9" fill="var(--cocoa)"/>
            <path d="M6.2 4.5l1.6 2.2-1 1.1c.6 1.3 1.6 2.3 2.9 2.9l1.1-1 2.2 1.6-.8 1.6c-3.6-.4-6.4-3.2-6.8-6.8z" fill="var(--sun)"/>
          </svg>
          <span>000 555 2748</span>
        </li>
        <li>
          <svg class="contact-icon" viewBox="0 0 18 18" aria-hidden="true">
            <circle cx="9" cy="9" r="9" fill="var(--cocoa)"/>
            <rect x="4.5" y="5.8" width="9" height="6.4" fill="none" stroke="var(--sun)" stroke-width="1.2"/>
            <path d="M4.5 5.8L9 9.4l4.5-3.6" fill="none" stroke="var(--sun)" stroke-width="1.2"/>
          </svg>
          <span>hello@tirovel.com</span>
        </li>
        <li>
          <svg class="contact-icon" viewBox="0 0 18 18" aria-hidden="true">
            <circle cx="9" cy="9" r="9" fill="var(--cocoa)"/>
            <circle cx="9" cy="9" r="5" fill="none" stroke="var(--sun)" stroke-width="1.1"/>
            <ellipse cx="9" cy="9" rx="2.2" ry="5" fill="none" stroke="var(--sun)" stroke-width="1.1"/>
            <path d="M4 9h10" stroke="var(--sun)" stroke-width="1.1"/>
          </svg>
          <span>www.tirovel.com</span>
        </li>
      </ul>
    </section>
  </article>
</main>
</body>
</html>
```